依頼詳細
ロゴデータをご参考ください。
主に取引企業との挨拶(営業)時の利用になります。
ロゴカラーがブルー色・オレンジ色ですが、ロゴカラーに沿うような表裏面共に統一性のあるシンプルテイストでお願いします。

それでいて、ひと目で印象に残るようなデザインを
よろしくお願いします。
記載項目
※表面のみでも裏面活用有りでも構いません。
※名刺の向きに関しまして特段指定はございません。
※名前の字数が3字・5字であってもバランスのとれるデザイン。

【会社名】ミナモリーフ株式会社
【役職】代表取締役
【名前】川村健二・KENJI KAWAMURA
【住所】〒650-0047 兵庫県神戸市中央区栄町通58-7 ハーバーテラス3F
【電話/FAX】TEL:000-111-2222 FAX:000-111-2223
【E-Mail】info@minamo-leaf.biz
【URL】http://www.minamo-leaf.org
希望イメージ
シンプル 複雑
単色 カラフル
暗い 明るい
日常 高級
遊び心 厳粛
未来的 伝統的
女性的 男性的
希望する色
ロゴカラー基調であれば特段指定無し。
納品ファイル
• 高解像度JPG (.jpg)
• イラストレーター形式 (.ai)
• フォトショップ形式 (.psd)
• PNG形式 (.png)
補足説明

折衝時の話題にできそうな斬新なアイデア、当社ロゴに沿った表記字体・配置のバランスなど、ひと目で印象に残せるようなデザインに感銘を受けました。
大変満足しております。

この度は、たくさんの素晴らしいデザインをご提案いただき、
誠にありがとうございました。
今後とも、各種ご依頼におきまして皆様の個性あふれる優れたアイデア
を以ってお力添えを頂ければと思います。

```html
<!DOCTYPE html>
<html lang="ja">
<head>
<meta charset="utf-8">
<title>ミナモリーフ株式会社 名刺</title>
<link href="https://fonts.googleapis.com/css2?family=Noto+Sans+JP:wght@400;500;700&display=swap" rel="stylesheet">
<style>
  :root {
    --stage: #dcdcdc;
    --card: #ffffff;
    --brand-blue: #1e7fd0;
    --brand-blue-deep: #1466b3;
    --ink: #222222;
    --ink-soft: #555555;
    --rule: #d8d8d8;
    --sky-top: #8fc3ea;
    --sky-mid: #c9e2f4;
    --sky-low: #eef6fc;
  }
  * { margin: 0; padding: 0; box-sizing: border-box; }
  html, body { width: 891px; height: 1200px; overflow: hidden; }
  body {
    background: var(--stage);
    font-family: "Noto Sans JP", sans-serif;
    color: var(--ink);
    position: relative;
  }
  .card {
    position: absolute;
    left: 113px;
    width: 665px;
    height: 402px;
    background: var(--card);
    overflow: hidden;
  }
  .card--front { top: 135px; }
  .card--back { top: 615px; }

  /* front */
  .brand {
    position: absolute;
    top: 56px;
    left: 0; right: 0;
    display: flex;
    justify-content: center;
    align-items: center;
    gap: 14px;
  }
  .brand__dot {
    width: 34px; height: 34px;
    border-radius: 50%;
    background: var(--brand-blue);
  }
  .brand__name {
    font-family: "Noto Sans JP", sans-serif;
    font-weight: 700;
    font-size: 34px;
    line-height: 1;
    letter-spacing: 2px;
    color: var(--ink);
  }
  .front-rule {
    position: absolute;
    top: 128px; left: 40px; right: 40px;
    border-top: 1px solid var(--rule);
  }
  .identity {
    position: absolute;
    left: 44px; top: 150px;
  }
  .identity__company { font-size: 20px; font-weight: 700; letter-spacing: 1px; }
  .identity__title { margin-top: 28px; font-size: 12px; color: var(--ink-soft); }
  .identity__name { margin-top: 4px; font-size: 34px; font-weight: 500; letter-spacing: 10px; }
  .identity__roman { margin-top: 2px; font-size: 10px; letter-spacing: 1px; color: var(--ink-soft); }

  .contact {
    position: absolute;
    left: 372px; top: 148px;
    font-size: 12.5px;
    line-height: 1.55;
    color: var(--ink);
  }
  .contact__address { margin-bottom: 4px; }
  .contact__row { display: flex; align-items: center; gap: 7px; }
  .contact__row svg { width: 13px; height: 13px; fill: var(--ink); flex: none; }

  .front-band {
    position: absolute;
    left: 0; right: 0; bottom: 0;
    height: 30px;
    background: linear-gradient(90deg, var(--brand-blue-deep), var(--brand-blue));
  }

  /* back */
  .sky {
    position: absolute; inset: 0;
    background: linear-gradient(180deg, var(--sky-top) 0%, var(--sky-mid) 45%, var(--sky-low) 100%);
  }
  .back-brand {
    position: absolute;
    top: 122px; left: 0; right: 0;
    display: flex;
    flex-direction: column;
    align-items: center;
    gap: 16px;
  }
  .back-brand__dot {
    width: 84px; height: 84px;
    border-radius: 50%;
    background: var(--brand-blue);
  }
  .back-brand__name {
    font-family: "Noto Sans JP", sans-serif;
    font-weight: 700;
    font-size: 28px;
    line-height: 1;
    letter-spacing: 2px;
    color: var(--ink);
  }
</style>
</head>
<body>

<section class="card card--front" aria-label="名刺 表面">
  <div class="brand">
    <span class="brand__dot"></span>
    <span class="brand__name">MINAMOLEAF</span>
  </div>
  <div class="front-rule"></div>

  <div class="identity">
    <p class="identity__company">ミナモリーフ株式会社</p>
    <p class="identity__title">代表取締役</p>
    <p class="identity__name">川村 健二</p>
    <p class="identity__roman">KENJI KAWAMURA</p>
  </div>

  <div class="contact">
    <div class="contact__address">
      <p>〒650-0047</p>
      <p>兵庫県神戸市中央区栄町通58-7</p>
      <p>ハーバーテラス3F</p>
    </div>
    <p class="contact__row">
      <svg viewBox="0 0 16 16" aria-hidden="true"><path d="M4 1l3 3-2 2c1 2 3 4 5 5l2-2 3 3-2 3C7 15 1 9 1 3z"/></svg>
      TEL:000-111-2222
    </p>
    <p class="contact__row">
      <svg viewBox="0 0 16 16" aria-hidden="true"><path d="M4 1h7v4H4zM1 6h14v7h-3v2H4v-2H1zm4 5v3h6v-3z"/></svg>
      FAX:000-111-2223
    </p>
    <p class="contact__row">
      <svg viewBox="0 0 16 16" aria-hidden="true"><path d="M1 3h14v10H1zm1.5 1.3V12h11V4.3L8 8.5z"/></svg>
      info@minamo-leaf.biz
    </p>
    <p class="contact__row">
      <svg viewBox="0 0 16 16" aria-hidden="true"><path d="M8 1a7 7 0 110 14A7 7 0 018 1zm0 1.5A5.5 5.5 0 002.6 7h10.8A5.5 5.5 0 008 2.5zM2.6 9A5.5 5.5 0 0013.4 9z"/></svg>
      http://www.minamo-leaf.org
    </p>
  </div>

  <div class="front-band"></div>
</section>

<section class="card card--back" aria-label="名刺 裏面">
  <div class="sky" role="img" aria-label="雲海の上に広がる明るい青空の写真"></div>
  <div class="back-brand">
    <span class="back-brand__dot"></span>
    <span class="back-brand__name">MINAMOLEAF</span>
  </div>
</section>

</body>
</html>
```